QRV Stationery Design Project

Dear Designers,
We need a new stationery design for company to match our new logo.
Designers should provide a design for the following:
1. Business Card: 3.5x2 Inches.
2. Letterhead: A4 size.
3. Envelops: 25x35.5 Cm.
You can keep the Arabic name at the bottom of the logo Or you can use the separate attached Arabic Name.
Please refer to the attached logo guide for design information.
Sample Business Card information:
Name: Tariq Nawaf
Position: Operation Manager
Tel: +966 920007714 Ex. 500
Fax: +966 (3)8842617
Mob: +966 (5)00387251
email: tariq@qrv-example.com.sa
URL: www.qrv-example.com.sa
Address:
Al Wadi Tower, Suite 303
Nasser bin Salem Str.
Khobar, 31847
Saudi Arabia
Updates
Dear All,
Please note, we had uploaded our logo along with Arabic writing in Adobe illustrator format (.ai).
Regards,
Khalid
Dear All,
A sample data for the business card had been added as per your request.
Regards,
Khalid

```html
<!DOCTYPE html>
<html lang="en">
<head>
<meta charset="utf-8">
<title>QRV Stationery</title>
<link rel="stylesheet" href="https://fonts.googleapis.com/css2?family=Open+Sans:wght@400;600;700&family=Noto+Serif:ital@1&display=swap">
<style>
:root{
  --navy:#0c2b4f;
  --grey:#8d9096;
  --grey-light:#b9bcc1;
  --paper:#ffffff;
  --paper-tint:#f4f5f7;
  --backdrop:#e6e8eb;
  --ink:#3b3f45;
}
*{box-sizing:border-box;margin:0;padding:0}
html,body{width:1200px;height:795px;overflow:hidden}
body{background:var(--backdrop);font-family:"Open Sans",Arial,sans-serif;color:var(--ink);position:relative}
.sheet{position:absolute;background:var(--paper);box-shadow:0 2px 8px rgba(0,0,0,.12);overflow:hidden}

.brand{display:flex;align-items:center;gap:6px;color:var(--navy);font-weight:700;letter-spacing:.5px;line-height:1;white-space:nowrap}
.brand .dot{width:.5em;height:.5em;border-radius:50%;background:var(--grey)}
.brand.on-dark{color:var(--paper)}
.brand.on-dark .dot{background:var(--grey-light)}

.contact{font-size:6px;line-height:1.7;color:var(--ink);white-space:nowrap}
.contact li{list-style:none;display:flex;align-items:center;gap:4px}
.contact svg{width:6px;height:6px;flex:none}

.footer-band{position:absolute;left:0;right:0;bottom:0}
.footer-band .rule{height:3px;background:var(--grey-light)}
.footer-band .bar{background:var(--navy)}

.card-front{left:60px;top:60px;width:220px;height:126px;background:var(--navy)}
.card-front .brand{position:absolute;left:30px;top:42px;font-size:26px}
.card-front .url{position:absolute;left:30px;top:80px;font-size:7px;color:var(--grey-light);letter-spacing:1.5px}

.card-back{left:60px;top:226px;width:220px;height:126px}
.card-back .brand{position:absolute;left:14px;top:14px;font-size:16px}
.card-back .contact{position:absolute;left:14px;top:44px;font-size:5.5px}
.card-back .person{position:absolute;right:14px;top:58px;text-align:right}
.card-back .person .name{font-size:8px;font-weight:700;color:var(--navy)}
.card-back .person .role{font-size:6px;color:var(--grey)}
.card-back .footer-band .bar{height:6px}

.letterhead{left:360px;top:30px;width:330px;height:467px}
.letterhead .brand{position:absolute;left:26px;top:26px;font-size:22px}
.letterhead .contact{position:absolute;right:28px;top:62px;font-size:5.5px}
.letterhead .edge-mark{position:absolute;right:0;top:90px;width:4px;height:28px;background:var(--navy)}
.letterhead .footer-band{bottom:18px}
.letterhead .footer-band .bar{height:7px}

.folder{left:780px;top:30px;width:330px;height:467px;background:var(--paper-tint)}
.folder .brand{position:absolute;left:0;right:0;top:92px;justify-content:center;font-size:46px}
.folder .url-band{position:absolute;left:0;right:0;top:196px;height:18px;background:var(--grey-light);display:flex;align-items:center;justify-content:center;font-size:8px;letter-spacing:2px;color:var(--paper)}
.folder .cover-panel{position:absolute;left:0;right:0;top:214px;bottom:0;background:var(--navy)}

.envelope{left:40px;top:550px;width:360px;height:180px}
.envelope .brand{position:absolute;left:22px;top:20px;font-size:20px}
.envelope .return{position:absolute;left:22px;top:48px;font-size:5.5px;color:var(--grey);white-space:nowrap}
.envelope .footer-band{bottom:22px}
.envelope .footer-band .bar{height:8px}

.slip{left:420px;top:550px;width:360px;height:180px}
.slip .brand{position:absolute;left:22px;top:20px;font-size:20px}
.slip .contact{position:absolute;right:22px;top:60px;font-size:5.5px}
.slip .greeting{position:absolute;left:22px;bottom:40px;font-family:"Noto Serif",Georgia,serif;font-style:italic;font-size:9px;color:var(--navy)}
.slip .edge-mark{position:absolute;right:0;bottom:30px;width:4px;height:22px;background:var(--navy)}
.slip .footer-band{bottom:18px}
.slip .footer-band .bar{height:7px}

.envelope-back{left:800px;top:550px;width:360px;height:180px}
.envelope-back .flap{position:absolute;left:0;right:0;top:0;height:74px;background:var(--navy);display:flex;align-items:center;justify-content:center}
.envelope-back .flap .brand{font-size:18px}
</style>
</head>
<body>

<svg width="0" height="0" style="position:absolute">
  <symbol id="icon-phone" viewBox="0 0 10 10"><circle cx="5" cy="5" r="5" fill="#8d9096"/><path d="M3.3 2.6l1 1-.5.7c.3.7.8 1.2 1.5 1.5l.7-.5 1 1-.7.9C4.6 7 3 5.4 2.8 3.3z" fill="#fff"/></symbol>
  <symbol id="icon-fax" viewBox="0 0 10 10"><circle cx="5" cy="5" r="5" fill="#8d9096"/><rect x="3" y="3" width="4" height="4" fill="#fff"/></symbol>
  <symbol id="icon-mail" viewBox="0 0 10 10"><circle cx="5" cy="5" r="5" fill="#8d9096"/><rect x="2.6" y="3.4" width="4.8" height="3.2" fill="#fff"/><path d="M2.6 3.4L5 5.2l2.4-1.8" stroke="#8d9096" stroke-width=".5" fill="none"/></symbol>
  <symbol id="icon-pin" viewBox="0 0 10 10"><circle cx="5" cy="5" r="5" fill="#8d9096"/><path d="M5 2.4a1.8 1.8 0 0 1 1.8 1.8C6.8 5.6 5 7.6 5 7.6S3.2 5.6 3.2 4.2A1.8 1.8 0 0 1 5 2.4z" fill="#fff"/></symbol>
</svg>

<section class="sheet card-front">
  <div class="brand on-dark"><span>QRV</span><span class="dot"></span></div>
  <p class="url">www.qrv-example.com.sa</p>
</section>

<section class="sheet card-back">
  <div class="brand"><span>QRV</span><span class="dot"></span></div>
  <ul class="contact">
    <li><svg><use href="#icon-phone"/></svg>+966 920007714 Ex. 500</li>
    <li><svg><use href="#icon-fax"/></svg>+966 (3)8842617</li>
    <li><svg><use href="#icon-phone"/></svg>+966 (5)00387251</li>
    <li><svg><use href="#icon-mail"/></svg>tariq@qrv-example.com.sa</li>
  </ul>
  <div class="person">
    <p class="name">Tariq Nawaf</p>
    <p class="role">Operation Manager</p>
  </div>
  <div class="footer-band"><div class="rule"></div><div class="bar"></div></div>
</section>

<section class="sheet letterhead">
  <div class="brand"><span>QRV</span><span class="dot"></span></div>
  <ul class="contact">
    <li><svg><use href="#icon-pin"/></svg>Al Wadi Tower, Suite 303</li>
    <li><svg><use href="#icon-pin"/></svg>Nasser bin Salem Str., Khobar 31847</li>
    <li><svg><use href="#icon-phone"/></svg>+966 920007714</li>
    <li><svg><use href="#icon-fax"/></svg>+966 (3)8842617</li>
    <li><svg><use href="#icon-mail"/></svg>www.qrv-example.com.sa</li>
  </ul>
  <div class="edge-mark"></div>
  <div class="footer-band"><div class="rule"></div><div class="bar"></div></div>
</section>

<section class="sheet folder">
  <div class="brand"><span>QRV</span><span class="dot"></span></div>
  <div class="url-band">www.qrv-example.com.sa</div>
  <div class="cover-panel"></div>
</section>

<section class="sheet envelope">
  <div class="brand"><span>QRV</span><span class="dot"></span></div>
  <p class="return">Al Wadi Tower, Suite 303, Nasser bin Salem Str., Khobar 31847, Saudi Arabia</p>
  <div class="footer-band"><div class="rule"></div><div class="bar"></div></div>
</section>

<section class="sheet slip">
  <div class="brand"><span>QRV</span><span class="dot"></span></div>
  <ul class="contact">
    <li><svg><use href="#icon-pin"/></svg>Al Wadi Tower, Suite 303</li>
    <li><svg><use href="#icon-pin"/></svg>Nasser bin Salem Str., Khobar 31847</li>
    <li><svg><use href="#icon-phone"/></svg>+966 920007714</li>
    <li><svg><use href="#icon-fax"/></svg>+966 (3)8842617</li>
    <li><svg><use href="#icon-mail"/></svg>www.qrv-example.com.sa</li>
  </ul>
  <p class="greeting">With Best Compliments</p>
  <div class="edge-mark"></div>
  <div class="footer-band"><div class="rule"></div><div class="bar"></div></div>
</section>

<section class="sheet envelope-back">
  <div class="flap">
    <div class="brand on-dark"><span>QRV</span><span class="dot"></span></div>
  </div>
</section>

</body>
</html>
```